Young Balance Support Network

We need a poster explaining that some children live with a disability called Vestibular Disorder. Feel free to ask question. We want you to respect our color code, same as our logo.

Here is our website : http://www.ybsnetwork.org/

We need to sensibilise people about this disability for children.

Industry/Entity Type

Charity

Font styles to use
Serif

Requirements
Must have
• 1. our logo (with all our details) + one of the photo of Marek
• 2. design showing a child with a dizziness for exemple
• 3. a title saying : Aidez-nous à changer la vie des enfants vivant avec un problème vestibulaire
• 4.include the text attached (information flyer YBSN)
• Poster size : 24"X 36"
Should not have
• wheel chair

```html
<!DOCTYPE html>
<html lang="en">
<head>
<meta charset="utf-8">
<title>Young Balance Support Network – Poster</title>
<link href="https://fonts.googleapis.com/css2?family=Archivo+Black&family=Lato:wght@400;700&family=Raleway:wght@700;800&display=swap" rel="stylesheet">
<style>
  :root {
    --orange: #fbb117;
    --navy: #0d3f5e;
    --sky: #29b8ea;
    --stripe: #27c0f0;
    --leaf: #8cc63f;
    --ink: #444444;
    --slate: #555555;
    --paper: #ffffff;
    --mist: #e3e3e3;
  }
  html, body { margin: 0; padding: 0; overflow: hidden; background: var(--paper); }
  .poster {
    position: relative;
    width: 927px;
    height: 1200px;
    overflow: hidden;
    background: linear-gradient(180deg, #ffffff 0%, #f4f4f4 30%, var(--mist) 60%, #ececec 82%, #fafafa 100%);
    font-family: "Lato", sans-serif;
  }
  .backdrop { position: absolute; left: 0; top: 0; }
  .title {
    position: absolute;
    left: 0; top: 64px;
    width: 927px;
    margin: 0;
    text-align: center;
    font-family: "Archivo Black", sans-serif;
    font-weight: 400;
    font-size: 60px;
    line-height: 74px;
    letter-spacing: 0.5px;
    color: var(--navy);
  }
  .news-heading {
    position: absolute;
    left: 80px; top: 338px;
    margin: 0;
    font-family: "Lato", sans-serif;
    font-weight: 400;
    color: var(--sky);
  }
  .news-heading .lead { display: block; font-size: 54px; line-height: 58px; font-weight: 700; }
  .news-heading .amount { display: block; font-size: 46px; line-height: 54px; }
  .news-body {
    position: absolute;
    left: 80px; top: 464px;
    width: 568px;
    font-size: 17.4px;
    line-height: 22.4px;
    color: var(--ink);
  }
  .news-body p { margin: 0 0 21px; }
  .brand {
    position: absolute;
    left: 650px; top: 352px;
    width: 210px;
    height: 292px;
    display: flex;
    flex-direction: column;
    align-items: center;
    justify-content: flex-end;
  }
  .brand-dot {
    width: 150px; height: 150px;
    border-radius: 50%;
    background: var(--sky);
    margin-bottom: 42px;
  }
  .brand-name {
    font-family: "Lato", sans-serif;
    font-weight: 700;
    font-size: 56px;
    line-height: 56px;
    letter-spacing: 7px;
    color: var(--leaf);
  }
  .appeal {
    position: absolute;
    left: 0; top: 678px;
    width: 927px;
    margin: 0;
    text-align: center;
    font-family: "Raleway", sans-serif;
    font-weight: 800;
    font-size: 30px;
    line-height: 36px;
    color: var(--slate);
  }
  .gallery { position: absolute; left: 0; top: 772px; }
  .contact {
    position: absolute;
    left: 80px; top: 1038px;
    font-family: "Archivo Black", sans-serif;
    font-size: 28px;
    line-height: 37px;
    color: var(--slate);
  }
  .contact div { white-space: nowrap; }
  .social {
    position: absolute;
    left: 616px; top: 1052px;
    display: flex;
    gap: 18px;
  }
  .social-tile {
    width: 82px; height: 86px;
    border-radius: 3px;
    display: flex;
    align-items: center;
    justify-content: center;
    font-family: "Lato", sans-serif;
    font-weight: 700;
    font-size: 14px;
    color: var(--paper);
  }
  .social-tile.linkbook { background: #3a5a9c; }
  .social-tile.chirper { background: #2aa3e6; }
</style>
</head>
<body>
<div class="poster">
  <svg class="backdrop" width="927" height="460" viewBox="0 0 927 460" aria-hidden="true">
    <defs>
      <linearGradient id="swoosh" x1="0" y1="0" x2="1" y2="0">
        <stop offset="0" stop-color="#c8c8c8"/>
        <stop offset="0.45" stop-color="#ffffff"/>
        <stop offset="1" stop-color="#8f8f8f"/>
      </linearGradient>
    </defs>
    <path d="M0 0 H927 V432 C850 332 700 262 520 250 C400 243 180 268 0 370 Z" fill="var(--orange)"/>
    <path d="M0 370 C180 268 400 243 520 250 C700 262 850 332 927 432 V452 C850 350 700 280 520 266 C400 259 180 284 0 390 Z" fill="url(#swoosh)"/>
  </svg>

  <h1 class="title">YOUNG BALANCE<br>SUPPORT NETWORK</h1>

  <h2 class="news-heading">
    <span class="lead">Great News</span>
    <span class="amount">CHF 3000.- collected</span>
  </h2>

  <div class="news-body">
    <p>Lucien, Nadira, Ondine and Bastien ran to support us. They took up the challenge of running 10km / 20km to support our association.</p>
    <p>They counted on you to sponsor their race and they targeted to get CHF 3'000.- ! We did it !</p>
    <p>This amount will help our association to raise awarness of this disability by publishing flyers and posters in Swiss and European hospitals !</p>
  </div>

  <div class="brand" aria-label="Young Balance Support Network">
    <div class="brand-dot"></div>
    <div class="brand-name">YBSN</div>
  </div>

  <p class="appeal" lang="fr">Aidez-nous à changer la vie des enfants vivant avec<br>un problème vestibulaire</p>

  <svg class="gallery" width="927" height="242" viewBox="0 0 927 242">
    <defs>
      <linearGradient id="photoPlay" x1="0" y1="0" x2="1" y2="1">
        <stop offset="0" stop-color="#8fa7b8"/>
        <stop offset="0.5" stop-color="#5f7a4a"/>
        <stop offset="1" stop-color="#a56f52"/>
      </linearGradient>
      <linearGradient id="photoDizzy" x1="0" y1="0" x2="1" y2="0">
        <stop offset="0" stop-color="#4d4f52"/>
        <stop offset="0.5" stop-color="#b59a84"/>
        <stop offset="1" stop-color="#6b6d70"/>
      </linearGradient>
      <linearGradient id="photoPark" x1="0" y1="0" x2="1" y2="1">
        <stop offset="0" stop-color="#9ab7c9"/>
        <stop offset="0.5" stop-color="#7b6a5c"/>
        <stop offset="1" stop-color="#5d7786"/>
      </linearGradient>
    </defs>
    <rect x="0" y="0" width="927" height="242" fill="var(--stripe)"/>
    <g role="img" aria-label="Photo of a child playing at a water park">
      <polygon points="0,20 336,20 290,224 0,224" fill="url(#photoPlay)"/>
    </g>
    <g role="img" aria-label="Photo of a child covering his ears, feeling dizzy">
      <polygon points="348,20 658,20 614,224 300,224" fill="url(#photoDizzy)"/>
    </g>
    <g role="img" aria-label="Photo of a smiling child with her mother at a splash park">
      <polygon points="670,20 927,20 927,224 626,224" fill="url(#photoPark)"/>
    </g>
  </svg>

  <div class="contact">
    <div>www.ybsnetwork.org</div>
    <div>info@ybsnetwork.org</div>
    <div>CCP: 25-408317-6</div>
  </div>

  <div class="social">
    <div class="social-tile linkbook">Linkbook</div>
    <div class="social-tile chirper">Chirper</div>
  </div>
</div>
</body>
</html>
```